New Property management company business cards

Looking for a new business card, to reflect new younger ownership
Card should be clean, simple and professional but with a modern layout that is conveys our new logo and business model

Key aspects of the business:

Property Management
Facility Maintenance
Project Management
Tenant Improvements

Mailing Address:
PO BOX 7186
Larkfield CA, 95812

Phone: 555-614-8837
Direct: 555-614-8831

Doyle Farrant
President

Target Market(s)

Commercial property owners

Industry/Entity Type

Real Estate property management

Contact Information for Business Card

Open to all designs but lean toward vertical layouts

Requirements
Must have
• Logo and space to customize name and contact info

```html
<!DOCTYPE html>
<html lang="en">
<head>
<meta charset="utf-8">
<title>Norvale Property Management – Business Card</title>
<link rel="stylesheet" href="https://fonts.googleapis.com/css2?family=Cabin+Condensed:wght@400;500;600&family=Montserrat:wght@500&display=swap">
<style>
  :root {
    --navy: #1b243b;
    --green: #43f396;
    --paper: #ffffff;
    --backdrop: #dadada;
  }
  * { margin: 0; padding: 0; box-sizing: border-box; }
  html, body { width: 1200px; height: 846px; overflow: hidden; }
  body {
    background: var(--backdrop);
    font-family: "Cabin Condensed", "Arial Narrow", sans-serif;
    position: relative;
  }
  .card {
    position: absolute;
    left: 346px;
    width: 508px;
    height: 290px;
    overflow: hidden;
  }
  .card--front { top: 99px; background: var(--paper); color: var(--navy); }
  .card--back { top: 457px; background: var(--navy); color: var(--green); }

  .front-graphic { position: absolute; left: 0; top: 0; }

  .line { position: absolute; left: 325px; white-space: nowrap; }

  .brand {
    position: absolute;
    left: 325px;
    width: 123px;
    top: 36px;
    text-align: center;
  }
  .brand__mark {
    display: block;
    width: 18px;
    height: 18px;
    margin: 0 auto 22px;
    background: var(--navy);
  }
  .brand__name {
    font-family: "Montserrat", sans-serif;
    font-weight: 500;
    font-size: 17px;
    letter-spacing: 3.6px;
    margin-right: -3.6px;
    line-height: 17px;
  }
  .brand__sub {
    font-family: "Montserrat", sans-serif;
    font-weight: 500;
    font-size: 5.6px;
    letter-spacing: 2.2px;
    margin-right: -2.2px;
    line-height: 8px;
    margin-top: 1px;
  }
  .person__name {
    top: 115px;
    color: var(--green);
    font-weight: 600;
    font-size: 21px;
    line-height: 24px;
  }
  .person__title { top: 136px; font-weight: 500; font-size: 12px; line-height: 16px; }
  .contact { font-size: 14px; line-height: 18px; }
  .contact--phone { top: 168px; }
  .contact--direct { top: 185px; }
  .address--box { top: 219px; }
  .address--city { top: 239px; }

  .back-mark {
    position: absolute;
    left: 78px;
    top: 130px;
    width: 60px;
    height: 60px;
    background: var(--green);
  }
  .back-name {
    position: absolute;
    left: 183px;
    top: 131px;
    font-family: "Montserrat", sans-serif;
    font-weight: 500;
    font-size: 40px;
    line-height: 42px;
    letter-spacing: 17px;
  }
  .back-sub {
    position: absolute;
    left: 185px;
    top: 172px;
    font-family: "Montserrat", sans-serif;
    font-weight: 500;
    font-size: 11.5px;
    line-height: 14px;
    letter-spacing: 8.9px;
  }
  .services {
    position: absolute;
    left: 46px;
    width: 418px;
    top: 237px;
    font-size: 10px;
    line-height: 14px;
    white-space: nowrap;
    display: flex;
    justify-content: space-between;
  }
</style>
</head>
<body>
  <section class="card card--front">
    <svg class="front-graphic" width="508" height="290" viewBox="0 0 508 290" aria-hidden="true">
      <polygon fill="var(--green)" points="0,46 102,148 0,250"/>
      <polygon fill="var(--navy)" points="60,0 115.5,0 263,148 123,290 67,290 208,148"/>
    </svg>
    <div class="brand">
      <span class="brand__mark"></span>
      <div class="brand__name">NORVALE</div>
      <div class="brand__sub">PROPERTY MANAGEMENT</div>
    </div>
    <div class="line person__name">Doyle Farrant</div>
    <div class="line person__title">President</div>
    <div class="line contact contact--phone">Phone: 555-614-8837</div>
    <div class="line contact contact--direct">Direct: 555-614-8831</div>
    <div class="line contact address--box">PO BOX 7186</div>
    <div class="line contact address--city">Larkfield CA, 95812</div>
  </section>

  <section class="card card--back">
    <span class="back-mark"></span>
    <div class="back-name">NORVALE</div>
    <div class="back-sub">PROPERTY MANAGEMENT</div>
    <p class="services">
      <span>PROPERTY MANAGEMENT</span><span>/</span>
      <span>FACILITY MAINTENANCE</span><span>/</span>
      <span>PROJECT MANAGEMENT</span><span>/</span>
      <span>TENANT IMPROVEMENTS</span>
    </p>
  </section>
</body>
</html>
```